website design for an energy technology company

Verdant Ridge Holdings is an African based company with interests in renewable energy, clean thermal power and building automation with an overall objective to ensure access to affordable, reliable, sustainable and modern energy for all.
The portal should be simple to navigate. Key attribute is to have scalable pictures of completed projects across the three different portfolios of Renewable energy, thermal power and building automation plus counters on megawatts of electricity.

Target Market(s)

Renewable energy, thermal power, building automation, smart building technology

Industry/Entity Type

Technology Equipment

Coding

Coded - Design and coding required

Number of Pages Required

5+ page

Font styles to use
Sans Serif

Colors
33a6d7
abd037
82c8e6
0255a3
33b8a4

Requirements
Must have
• Photos with human models must feature African males and females at the forefront.
We need counters on the first page and these should be represent installed base for (1) renewables-KW, (2) thermal - (kW), (3) carbon footprint saved
Nice to have
• Would like to have design that is as simple as www.plorvex.com. With this the left hand roulette style texts will include:
Renewables - This page will now have sub menus on:
Residential Solar
Commercial building solar
Solar Rural Electrification
Windmill
Sustainable technologies

Thermal - will have sub menus like below:
Plant Operation and maintenance
Captive Power Installation

Building Automation - will have sub-menus like:
Commercial building automation
Residential Building Automation
Products
Commercial packages
Services

KQT4 News (connected to the Orvane Shared Progress Aims)
Blogs
In The News
Should not have
• snow, nuclear power

```html
<!DOCTYPE html>
<html lang="en">
<head>
<meta charset="utf-8">
<title>Verdant Ridge Holdings</title>
<link href="https://fonts.googleapis.com/css2?family=Oswald:wght@500;600&family=Roboto:wght@400;500;700&display=swap" rel="stylesheet">
<style>
:root{
  --ink:#1b1a20;
  --blue:#1e93c2;
  --blue-deep:#1378a4;
  --navy:#0255a3;
  --text:#4a4a4a;
  --muted:#6a6a72;
  --card:#eeeeee;
  --white:#ffffff;
}
*{margin:0;padding:0;box-sizing:border-box}
html,body{width:1200px;height:5133px;overflow:hidden}
body{position:relative;background:var(--white);font-family:'Roboto',sans-serif;color:var(--text)}
.abs{position:absolute}
.display{font-family:'Oswald',sans-serif;text-transform:uppercase;color:var(--ink);font-weight:600}

/* header */
.site-header{left:0;top:0;width:1200px;height:128px;background:var(--ink)}
.brand{display:flex;align-items:center;gap:14px}
.brand-mark{width:44px;height:44px;border-radius:50%;background:var(--blue)}
.brand-name{font-family:'Oswald',sans-serif;font-weight:500;color:var(--white);font-size:18px;line-height:23px;text-transform:uppercase}
.phone{right:118px;top:26px;display:flex;align-items:center;gap:12px;font-family:'Oswald',sans-serif;font-weight:500;font-size:23px;color:var(--white)}
.phone-ico{width:36px;height:36px;border-radius:50%;background:var(--blue);display:flex;align-items:center;justify-content:center}
.main-nav{right:110px;top:82px;display:flex;gap:46px;font-family:'Oswald',sans-serif;font-weight:500;font-size:17px;color:var(--white);text-transform:uppercase}
.main-nav .active{color:var(--blue);border-bottom:2px solid var(--blue);padding-bottom:4px}

/* hero */
.hero{left:0;top:128px;width:1200px;height:700px;background:linear-gradient(180deg,#3c3a3e 0%,#6e655b 35%,#b88b55 58%,#7a6a3c 70%,#5d5230 100%)}
.hero-title{left:0;top:300px;width:1200px;text-align:center;font-family:'Oswald',sans-serif;font-weight:600;font-size:74px;line-height:74px;color:var(--white);text-transform:uppercase}
.btn{display:inline-block;border-radius:22px;font-family:'Roboto',sans-serif;font-weight:500}
.btn-hero{left:532px;top:472px;width:136px;height:44px;line-height:40px;text-align:center;background:var(--blue);color:var(--white);border:2px solid var(--white);font-size:14px;text-transform:uppercase}
.dots{left:563px;top:760px;display:flex;gap:6px}
.dots span{width:6px;height:6px;border-radius:50%;background:var(--white)}

/* installed base counters */
.counters{left:240px;top:580px;width:720px;display:flex;justify-content:space-between}
.counter{width:220px;text-align:center;color:var(--white)}
.counter + .counter{border-left:1px solid rgba(255,255,255,.35)}
.counter-value{font-family:'Oswald',sans-serif;font-weight:600;font-size:40px;line-height:48px}
.counter-value small{font-size:20px;font-weight:500;margin-left:4px}
.counter-label{font-size:13px;font-weight:500;line-height:20px;text-transform:uppercase;letter-spacing:.5px}

.section-title{left:0;width:1200px;text-align:center;font-size:50px;line-height:60px}
.section-lead{left:270px;width:660px;text-align:center;font-size:15px;line-height:26px;color:var(--text)}

/* services */
.ring{border-radius:50%;background:var(--blue)}
.photo{border-radius:50%}
.service h3{font-family:'Roboto',sans-serif;font-weight:500;font-size:36px;color:var(--ink)}
.service .rule{width:64px;height:3px;background:var(--navy);margin:22px 0 24px}
.service p{font-size:15px;line-height:26px;width:430px}
.btn-outline{margin-top:18px;padding:0 18px;height:40px;line-height:36px;border:2px solid var(--blue);color:var(--blue-deep);font-size:15px}

/* why */
.why-title{left:110px;top:2830px;font-size:52px;line-height:60px;color:var(--white)}
.why-text{left:110px;top:2965px;width:330px;font-size:14px;line-height:27px;color:#d8d8dc}
.feature{display:flex;gap:12px;width:300px}
.feature-ico{width:36px;height:36px;flex:none}
.feature h4{font-size:14px;font-weight:500;color:var(--white);margin-bottom:6px}
.feature p{font-size:12px;line-height:20px;color:#6d6d78}

/* news */
.news-card{top:3635px;width:310px;height:420px;background:var(--card)}
.news-photo{width:310px;height:206px}
.date{position:absolute;left:36px;top:240px;background:var(--blue);color:var(--white);font-size:13px;font-weight:500;padding:4px 10px}
.news-card h3{position:absolute;left:36px;top:292px;width:250px;font-size:18px;font-weight:500;line-height:29px;color:#555}
.news-card .arrow{position:absolute;left:36px;top:386px}

/* cta */
.cta-band{left:0;top:4150px;width:1200px;height:500px;background:linear-gradient(180deg,#1a7fae,#1f8fbe)}
.cta-text{left:0;top:4388px;width:1200px;text-align:center;font-family:'Oswald',sans-serif;font-weight:500;font-size:24px;line-height:41px;color:var(--white);text-transform:uppercase}
.btn-dark{left:514px;top:4478px;width:172px;height:44px;line-height:44px;text-align:center;background:var(--ink);color:var(--white);font-size:15px}

/* footer */
.social{right:110px;top:4704px;display:flex;gap:8px}
.social span{width:26px;height:26px;border-radius:50%;background:var(--blue)}
.divider{left:110px;width:980px;height:1px;background:#e2e2e2}
.foot-col{top:4822px}
.foot-col h5{font-family:'Oswald',sans-serif;font-weight:500;font-size:15px;text-transform:uppercase;color:var(--ink);margin-bottom:18px}
.foot-col li{list-style:none;font-size:14px;line-height:25px;color:#444}
.contact-row{display:flex;gap:16px;font-size:14px;line-height:22px;color:#444;margin-bottom:18px}
.copyright{left:0;top:5090px;width:1200px;text-align:center;font-size:14px;color:#444}
</style>
</head>
<body>

<header class="site-header abs">
  <div class="brand abs" style="left:110px;top:24px">
    <span class="brand-mark"></span>
    <span class="brand-name">Verdant Ridge<br>Holdings</span>
  </div>
  <div class="phone abs">
    <span class="phone-ico"><svg width="18" height="18" viewBox="0 0 24 24"><path fill="#fff" d="M6.6 10.8a15 15 0 0 0 6.6 6.6l2.2-2.2c.3-.3.7-.4 1-.2 1.1.4 2.3.6 3.6.6.6 0 1 .4 1 1V20c0 .6-.4 1-1 1A17 17 0 0 1 3 4c0-.6.4-1 1-1h3.5c.6 0 1 .4 1 1 0 1.3.2 2.5.6 3.6.1.3 0 .7-.2 1z"/></svg></span>
    PH: 0400 555 018
  </div>
  <nav class="main-nav abs">
    <span class="active">Home</span><span>Services</span><span>Works</span><span>Team</span><span>About</span><span>Contact</span>
  </nav>
</header>

<section class="hero abs" role="img" aria-label="Wind turbines over a wheat field at sunset"></section>
<svg class="abs" style="left:0;top:700px" width="1200" height="140" viewBox="0 0 1200 140">
  <path d="M0 60 Q600 120 1200 40 V140 H0 Z" fill="#fff"/>
  <path d="M110 88 Q600 125 1090 80 Q600 112 110 88 Z" fill="#1e93c2"/>
  <path d="M60 80 Q600 135 1140 70" stroke="#1e93c2" stroke-width="6" fill="none"/>
</svg>
<h1 class="hero-title abs">Energy Efficiency<br>and Sufficiency</h1>
<span class="btn btn-hero abs">Read More</span>

<div class="counters abs">
  <div class="counter"><div class="counter-value">12,480<small>kW</small></div><div class="counter-label">Renewables installed</div></div>
  <div class="counter"><div class="counter-value">36,250<small>kW</small></div><div class="counter-label">Thermal installed</div></div>
  <div class="counter"><div class="counter-value">8,920<small>t CO₂</small></div><div class="counter-label">Carbon footprint saved</div></div>
</div>

<div class="dots abs"><span></span><span></span><span></span><span></span><span></span></div>

<h2 class="section-title display abs" style="top:886px">Our Services</h2>
<p class="section-lead abs" style="top:964px">Sed ut perspiciatis unde omnis iste natus error sit voluptatem accusantium doloremque laudantium, totam rem aperiam, eaque ipsa quae ab illo inventore veritatis Sed ut perspiciatis unde omnis iste natus error sit voluptatem accusantium doloremque laudantium</p>

<!-- service 1 -->
<div class="ring abs" style="left:-40px;top:1082px;width:602px;height:602px"></div>
<div class="photo abs" role="img" aria-label="Wind turbines at dusk" style="left:-42px;top:1068px;width:586px;height:586px;background:linear-gradient(180deg,#4a4d58 0%,#8a7f78 45%,#6b6a66 70%,#2e2e2c 100%)"></div>
<div class="service abs" style="left:656px;top:1230px">
  <h3>Renewable energy</h3><div class="rule"></div>
  <p>Sed ut perspiciatis unde omnis iste natus error sit voluptatem accusantium doloremque laudantium, totam rem aperiam, eaque ipsa quae ab illo inventore veritatis</p>
  <span class="btn btn-outline">Read More</span>
</div>

<!-- service 2 -->
<div class="ring abs" style="left:628px;top:1494px;width:604px;height:604px"></div>
<div class="photo abs" role="img" aria-label="Thermal power plant cooling towers at dusk" style="left:646px;top:1478px;width:590px;height:590px;background:linear-gradient(180deg,#5a86c0 0%,#f0c27a 22%,#6c7a94 45%,#3c4a5c 75%,#2a3440 100%)"></div>
<div class="service abs" style="left:110px;top:1740px">
  <h3>Thermal Power</h3><div class="rule"></div>
  <p>Sed ut perspiciatis unde omnis iste natus error sit voluptatem accusantium doloremque laudantium, totam rem aperiam, eaque ipsa quae ab illo inventore veritatis</p>
  <span class="btn btn-outline">Read More</span>
</div>

<!-- why section background -->
<svg class="abs" style="left:0;top:2540px" width="1200" height="850" viewBox="0 0 1200 850">
  <path d="M0 110 Q700 70 1200 0 V850 H0 Z" fill="#1b1a20"/>
</svg>

<!-- service 3 -->
<div class="ring abs" style="left:-40px;top:2040px;width:602px;height:602px"></div>
<div class="photo abs" role="img" aria-label="Hands holding a tablet projecting a glowing building model" style="left:-42px;top:2026px;width:586px;height:586px;background:radial-gradient(circle at 40% 40%,#8fb0d6 0%,#33507c 40%,#141c30 80%)"></div>
<div class="service abs" style="left:656px;top:2190px">
  <h3>Building Automation</h3><div class="rule"></div>
  <p>Sed ut perspiciatis unde omnis iste natus error sit voluptatem accusantium doloremque laudantium, totam rem aperiam, eaque ipsa quae ab illo inventore veritatis</p>
  <span class="btn btn-outline">Read More</span>
</div>

<h2 class="why-title display abs">Why<br>Choose Us?</h2>
<p class="why-text abs">Sed ut perspiciatis unde omnis iste natus error sitvoluptatem accusantium doloremque laudantium, tota m rem aperiam, eaque ipsa quaeab illo inventore veratis Sed ut perspiciatis unde omnis iste natus error luptatem accusantium dolore.</p>

<svg class="abs" style="left:500px;top:2770px" width="340" height="500" viewBox="0 0 340 500">
  <g stroke="#8a8a94" stroke-width="1.2" fill="none">
    <path d="M172 20 V470 H320"/>
    <path d="M172 20 H320"/>
    <path d="M180 160 V120 H200"/>
    <path d="M215 260 V320 H200"/>
    <path d="M170 250 H255"/>
    <path d="M172 150 H180"/>
  </g>
  <g fill="#fff">
    <circle cx="172" cy="160" r="3"/><circle cx="185" cy="222" r="3"/><circle cx="255" cy="250" r="3"/><circle cx="188" cy="282" r="3"/><circle cx="180" cy="340" r="3"/>
  </g>
  <circle cx="85" cy="250" r="76" fill="#1e93c2"/>
  <circle cx="85" cy="250" r="48" fill="#1b1a20"/>
</svg>

<div class="feature abs" style="left:820px;top:2768px">
  <svg class="feature-ico" viewBox="0 0 36 36"><path d="M4 30V18L18 8l14 10v12z" fill="none" stroke="#1e93c2" stroke-width="2"/></svg>
  <div><h4>Industrial &amp; Residential solar</h4><p>Sed ut perspiciatis unde omnis iste natus error sit voluptatem</p></div>
</div>
<div class="feature abs" style="left:718px;top:2866px">
  <svg class="feature-ico" viewBox="0 0 36 36"><circle cx="18" cy="18" r="14" fill="none" stroke="#1e93c2" stroke-width="2"/></svg>
  <div><h4>Large and small wind turbines</h4><p>Sed ut perspiciatis unde omnis iste natus error sit voluptatem</p></div>
</div>
<div class="feature abs" style="left:806px;top:2972px">
  <svg class="feature-ico" viewBox="0 0 36 36"><path d="M4 32V18L18 6l14 12v14H22V22h-8v10z" fill="none" stroke="#1e93c2" stroke-width="2"/></svg>
  <div><h4>Commercial and Residential</h4><p>Sed ut perspiciatis unde omnis iste natus error sit voluptatem</p></div>
</div>
<div class="feature abs" style="left:732px;top:3098px">
  <svg class="feature-ico" viewBox="0 0 36 36"><circle cx="18" cy="18" r="12" fill="none" stroke="#1e93c2" stroke-width="3" stroke-dasharray="5 3"/><circle cx="18" cy="18" r="5" fill="none" stroke="#1e93c2" stroke-width="2"/></svg>
  <div><h4>Analytics/Big data</h4><p>Sed ut perspiciatis unde omnis iste natus error sit voluptatem</p></div>
</div>
<div class="feature abs" style="left:826px;top:3210px">
  <svg class="feature-ico" viewBox="0 0 36 36"><path d="M18 4a10 10 0 0 0-6 18v6h12v-6A10 10 0 0 0 18 4zM13 32h10" fill="none" stroke="#1e93c2" stroke-width="2"/></svg>
  <div><h4>Facility Management</h4><p>Sed ut perspiciatis unde omnis iste natus error sit voluptatem</p></div>
</div>

<h2 class="section-title display abs" style="top:3474px">Latest News</h2>
<p class="section-lead abs" style="top:3548px">Sed ut perspiciatis unde omnis iste natus error sit voluptatem accusantium doloremque laudantium, totam rem aperiam, eaque ipsa quae ab illo inventore veritatised ut perspiciati</p>

<article class="news-card abs" style="left:112px">
  <div class="news-photo" role="img" aria-label="Modern house with solar roof at dusk" style="background:linear-gradient(180deg,#7c93ad,#4b5a5a 60%,#3b4a2e)"></div>
  <span class="date">&#9633; MAY 12 2020</span>
  <h3>Lorem ipsum dolor sit alrt conse ctetur adipiscingld do eiusmod tem</h3>
  <svg class="arrow" width="32" height="10" viewBox="0 0 32 10"><path d="M0 5h30M25 1l5 4-5 4" stroke="#222" fill="none" stroke-width="1.5"/></svg>
</article>
<article class="news-card abs" style="left:446px">
  <div class="news-photo" role="img" aria-label="Power station chimneys reflected in water at dusk" style="background:linear-gradient(180deg,#b48db2,#e39a9a 45%,#5a5464 70%,#2c2c3a)"></div>
  <span class="date">&#9633; MAY 12 2020</span>
  <h3>Lorem ipsum dolor sit alrt conse ctetur adipiscingld do eiusmod tem</h3>
  <svg class="arrow" width="32" height="10" viewBox="0 0 32 10"><path d="M0 5h30M25 1l5 4-5 4" stroke="#222" fill="none" stroke-width="1.5"/></svg>
</article>
<article class="news-card abs" style="left:780px">
  <div class="news-photo" role="img" aria-label="Solar panel field below hills" style="background:linear-gradient(180deg,#a8b6c4,#c9a06c 50%,#8a6a44 75%,#b07a3c)"></div>
  <span class="date">&#9633; MAY 12 2020</span>
  <h3>Lorem ipsum dolor sit alrt conse ctetur adipiscingld do eiusmod tem</h3>
  <svg class="arrow" width="32" height="10" viewBox="0 0 32 10"><path d="M0 5h30M25 1l5 4-5 4" stroke="#222" fill="none" stroke-width="1.5"/></svg>
</article>

<div class="cta-band abs" role="img" aria-label="Industrial refinery skyline in blue tint"></div>
<svg class="abs" style="left:0;top:4140px" width="1200" height="120" viewBox="0 0 1200 120">
  <path d="M0 0 H1200 V25 Q600 100 0 55 Z" fill="#fff"/>
  <path d="M0 55 Q600 100 1200 25 V50 Q620 120 0 80 Z" fill="#1b1a20"/>
  <path d="M0 80 Q620 120 1200 50 V60 Q620 135 0 90 Z" fill="#fff"/>
</svg>
<p class="cta-text abs">Sed ut perspiciatis unde omnis iste natus error sit voluptatem<br>accusantium doloremque laudantium, totam rem aperia</p>
<span class="btn btn-dark abs">GET STARTED</span>

<footer>
  <div class="brand abs" style="left:110px;top:4700px">
    <span class="brand-mark" style="width:40px;height:40px"></span>
    <span class="brand-name" style="color:var(--ink);font-size:15px;line-height:19px">Verdant Ridge<br>Holdings</span>
  </div>
  <div class="social abs"><span></span><span></span><span></span></div>
  <div class="divider abs" style="top:4780px"></div>

  <div class="foot-col abs" style="left:110px">
    <h5>Contact</h5>
    <div class="contact-row"><svg width="22" height="22" viewBox="0 0 24 24"><path d="M12 2a7 7 0 0 0-7 7c0 5 7 13 7 13s7-8 7-13a7 7 0 0 0-7-7z" fill="none" stroke="#1e93c2" stroke-width="1.5"/><circle cx="12" cy="9" r="2.5" fill="none" stroke="#1e93c2" stroke-width="1.5"/></svg><span>12 Meridian Lane,<br>Harbour Quarter</span></div>
    <div class="contact-row"><svg width="22" height="22" viewBox="0 0 24 24"><path d="M6.6 10.8a15 15 0 0 0 6.6 6.6l2.2-2.2c.3-.3.7-.4 1-.2 1.1.4 2.3.6 3.6.6.6 0 1 .4 1 1V20c0 .6-.4 1-1 1A17 17 0 0 1 3 4c0-.6.4-1 1-1h3.5c.6 0 1 .4 1 1 0 1.3.2 2.5.6 3.6.1.3 0 .7-.2 1z" fill="none" stroke="#1e93c2" stroke-width="1.5"/></svg><span>8 800 555 014 22<br>8 800 555 027 63</span></div>
    <div class="contact-row"><svg width="22" height="22" viewBox="0 0 24 24"><rect x="2" y="5" width="20" height="14" fill="none" stroke="#1e93c2" stroke-width="1.5"/><path d="M2 5l10 8 10-8" fill="none" stroke="#1e93c2" stroke-width="1.5"/></svg><span>info@verdantridge.com<br>founder@verdantridge.com</span></div>
  </div>
  <div class="foot-col abs" style="left:414px">
    <h5>Company</h5>
    <ul><li>Lorem ipsum dolo</li><li>Fusce eget leo tincid</li><li>Donec consequat</li><li>Praesent elementum</li><li>Jmauris posueret</li><li>Aenean a ex eu lectu</li><li>Donec consequa</li></ul>
  </div>
  <div class="foot-col abs" style="left:680px">
    <h5>Projects</h5>
    <ul><li>Lorem ipsum dolo</li><li>Fusce eget leo tincid</li><li>Donec consequat</li><li>Praesent elementum</li><li>Jmauris posueret</li><li>Donec consequa</li><li>Aenean a ex eu lectu</li></ul>
  </div>
  <div class="foot-col abs" style="left:924px">
    <h5>Other Links</h5>
    <ul><li>Lorem ipsum dolo</li><li>Consecteturipiscinit</li><li>Fusce eget leo tincid</li><li>Praesent elementum</li><li>Jmauris posueret</li><li>Donec consequa</li><li>Aenean a ex eu lectu</li></ul>
  </div>
  <div class="divider abs" style="top:5064px"></div>
  <p class="copyright abs">Copyright 2020 Verdant Ridge Holdings . All Rights Reserved</p>
</footer>

</body>
</html>
```